Mrs Tully's Menu Design

Our website is MrsTullys.com.au
Please take inspiration in the look and feel, style and tone from the photos of our takeaway restaurant.

We' have been providing our famous Chinese take away in Merrylands for over 30 years. We have seen the neighbourhood grow around us and we have grown along with them.
We have had a recent shopfitting (see photos on http://www.mrstullys.com.au).

Red features prominently in our shop design but understand if you would keep it muted or minimal for readability.

We would like to revamp our plain menu to a fresh new look with a typeface that emphasizes familiarity and simple, delicious food.

Reason: Updated brief with more information Would like more designs

Target Market(s)

Our customers are locals who have enjoyed our famous Chinese takeaway for over 30 years. They are mums buying takeout for their family dinner, staff from the surrounding mall shops after a quick, delicious feed and regulars who come in every week for their fix of freshly prepared, familiar Chinese favourites like san choy bow, crispy salt and pepper squid and stir-fried beef in black bean sauce.

Industry/Entity Type

Shop

Requirements
Must have
• Typeface is very important.
It must be readable and convey a classic Chinese menu that oozes familiarity and sincerity. We serve simple, classic Chinese favorites at a economical price
Should not have
• Should not be childish, cartoony or cliched.

```html
<!DOCTYPE html>
<html lang="en">
<head>
<meta charset="utf-8">
<title>Mrs Tully's Chinese Kitchen Menu</title>
<link rel="stylesheet" href="https://fonts.googleapis.com/css2?family=Ubuntu:ital,wght@0,400;0,500;0,700;1,700&family=Ubuntu+Condensed&display=swap">
<style>
  :root {
    --red: #d71920;
    --red-deep: #a80f15;
    --black: #111111;
    --white: #ffffff;
    --cream: #f3ece1;
    --stone: #d9cfc2;
  }
  * { box-sizing: border-box; margin: 0; padding: 0; }
  html, body {
    width: 1200px; height: 2400px; overflow: hidden;
    background: var(--red);
  }
  .menu {
    position: relative;
    width: 1200px; height: 2400px;
    background: var(--red);
    font-family: "Ubuntu Condensed", "Arial Narrow", sans-serif;
    color: var(--white);
    overflow: hidden;
  }
  .menu-frame {
    position: absolute; inset: 14px;
    border: 3px solid var(--white);
    outline: 10px solid var(--black);
    outline-offset: -13px;
    pointer-events: none;
  }
  .brand {
    position: absolute; left: 80px; top: 60px; width: 1040px;
  }
  .brand-name {
    font-family: "Ubuntu", sans-serif;
    font-weight: 700;
    font-size: 170px;
    line-height: 1;
    letter-spacing: -2px;
  }
  .brand-tagline {
    font-family: "Ubuntu", sans-serif;
    font-weight: 400;
    font-size: 40px;
    margin: 6px 0 0 540px;
  }
  .column-divider {
    position: absolute; left: 614px; top: 420px; height: 1880px;
    border-left: 4px dotted var(--white);
  }
  .section { position: absolute; top: var(--top); }
  .column-left .section { left: 60px; width: 536px; }
  .column-right .section { left: 640px; width: 520px; }
  .section-title {
    font-family: "Ubuntu", sans-serif;
    font-weight: 700;
    font-size: 31px;
    line-height: 36px;
  }
  .section-title.light { font-weight: 400; }
  .items { list-style: none; }
  .item {
    display: flex; align-items: baseline;
    font-size: 21px; line-height: 24.6px;
  }
  .item-name { white-space: nowrap; }
  .item-name small { font-size: 13px; }
  .leader {
    flex: 1; min-width: 6px; margin: 0 4px;
    border-bottom: 2px dotted var(--white);
    transform: translateY(-5px);
  }
  .price { white-space: nowrap; }
  .item-note {
    display: flex; align-items: baseline;
    font-size: 14px; line-height: 24.6px; padding-left: 22px;
  }
  .item-note .leader { transform: translateY(-4px); }
  .item-note .price { font-size: 21px; }
  .serving-note {
    position: absolute; left: 100px; top: 2302px; width: 830px;
    font-family: "Ubuntu", sans-serif;
    font-weight: 700; font-style: italic;
    font-size: 23px; line-height: 30px;
    text-align: right;
  }
  .guardian-art {
    position: absolute; left: 800px; top: 2160px; width: 370px; height: 140px;
  }
  .established {
    position: absolute; left: 950px; top: 2318px; width: 120px;
    font-family: "Ubuntu", sans-serif; font-size: 20px;
    text-align: center;
  }
</style>
</head>
<body>
<main class="menu">
  <div class="menu-frame"></div>

  <header class="brand">
    <h1 class="brand-name">Mrs Tully's</h1>
    <p class="brand-tagline">Chinese Kitchen</p>
  </header>

  <div class="column-divider"></div>

  <div class="column column-left">
    <section class="section" style="--top:380px">
      <h2 class="section-title">Mrs Tully's Specials</h2>
      <ul class="items">
        <li class="item"><span class="item-name">Golden Fried Box</span></li>
        <li class="item-note"><span class="item-name">Regular (1 Spring Roll, 1 Curry Meat Pastry, 2 Dim Sims, 1 Prawn Cutlet)</span><span class="leader"></span></li>
        <li class="item"><span class="price">$6.50</span></li>
        <li class="item-note"><span class="item-name">Large (1 Spring Roll, 1 Curry Meat Pastry, 4 Dim Sims, 2 Prawn Cutlets)</span><span class="leader"></span></li>
        <li class="item"><span class="price">$9.50</span></li>
        <li class="item"><span class="item-name">Seafood Combination with Oyster Sauce</span></li>
        <li class="item-note"><span class="item-name">(King Prawn, Scallop, Calamari, Mushrooms &amp; Babycorn)</span><span class="leader"></span><span class="price">$12.00</span></li>
        <li class="item"><span class="item-name">Sate Combination <small>(Beef, Chicken &amp; King Prawn)</small></span><span class="leader"></span><span class="price">$11.00</span></li>
        <li class="item"><span class="item-name">Garlic &amp; Chilli Combination <small>(Beef, Chicken &amp; King Prawn)</small></span><span class="leader"></span><span class="price">$11.00</span></li>
        <li class="item"><span class="item-name">Combination in Oyster Sauce <small>(Beef, Chicken &amp; King Prawn)</small></span><span class="leader"></span><span class="price">$11.00</span></li>
        <li class="item"><span class="item-name">Mongolian Lamb Fillet</span><span class="leader"></span><span class="price">$10.80</span></li>
        <li class="item"><span class="item-name">Deep Fried Lamb Fillet with Special Sauce</span><span class="leader"></span><span class="price">$10.80</span></li>
        <li class="item"><span class="item-name">Braised Chicken with Szechuan Sauce (Hot)</span><span class="leader"></span><span class="price">$9.90</span></li>
        <li class="item"><span class="item-name">Braised Chicken with Sweet Chilli Sauce</span><span class="leader"></span><span class="price">$9.90</span></li>
        <li class="item"><span class="item-name">Salt &amp; Pepper Squid</span><span class="leader"></span><span class="price">$10.00</span></li>
        <li class="item"><span class="item-name">Singapore Fried Noodles</span><span class="leader"></span><span class="price">$8.50</span></li>
      </ul>
    </section>

    <section class="section" style="--top:828px">
      <h2 class="section-title">Entré</h2>
      <ul class="items">
        <li class="item"><span class="item-name">Mini Spring Rolls (6)</span><span class="leader"></span><span class="price">$5.50</span></li>
        <li class="item"><span class="item-name">Spring Roll</span><span class="leader"></span><span class="price">$1.50</span></li>
        <li class="item"><span class="item-name">Curried Meat Pastry</span><span class="leader"></span><span class="price">$1.50</span></li>
        <li class="item"><span class="item-name">Dim Sim (Deep Fried)</span><span class="leader"></span><span class="price">$1.00</span></li>
        <li class="item"><span class="item-name">Dim Sims (Steamed) (6)</span><span class="leader"></span><span class="price">$5.50</span></li>
        <li class="item"><span class="item-name">Prawn Cutlet ............ (each) $1.70 .... (6)</span><span class="leader"></span><span class="price">$9.90</span></li>
        <li class="item"><span class="item-name">Chicken Wings (Deep Fried)</span><span class="leader"></span><span class="price">$5.50</span></li>
      </ul>
    </section>

    <section class="section" style="--top:1056px">
      <h2 class="section-title">Soup</h2>
      <ul class="items">
        <li class="item"><span class="item-name">Hot &amp; Sour Soup</span><span class="leader"></span><span class="price">Small $4.80 ... Large $6.80</span></li>
        <li class="item"><span class="item-name">Short Soup</span><span class="leader"></span><span class="price">$4.00</span></li>
        <li class="item"><span class="item-name">Long Soup</span><span class="leader"></span><span class="price">$4.00</span></li>
        <li class="item"><span class="item-name">Combination Soup</span><span class="leader"></span><span class="price">$4.00</span></li>
        <li class="item"><span class="item-name">Combination Long Soup</span><span class="leader"></span><span class="price">$7.00</span></li>
        <li class="item"><span class="item-name">Combination Short Soup</span><span class="leader"></span><span class="price">$7.00</span></li>
        <li class="item"><span class="item-name">Mixed Short &amp; Long Soup</span><span class="leader"></span><span class="price">$7.00</span></li>
        <li class="item"><span class="item-name">Sweet Corn Crab Meat Soup</span><span class="leader"></span><span class="price">$4.50</span></li>
        <li class="item"><span class="item-name">Chicken Sweet Corn Soup</span><span class="leader"></span><span class="price">$4.50</span></li>
      </ul>
    </section>

    <section class="section" style="--top:1328px">
      <h2 class="section-title">Sweet &amp; Sour</h2>
      <ul class="items">
        <li class="item"><span class="item-name">Sweet &amp; Sour Pork</span><span class="leader"></span><span class="price">$8.80</span></li>
        <li class="item"><span class="item-name">Sweet &amp; Sour Beef</span><span class="leader"></span><span class="price">$9.90</span></li>
        <li class="item"><span class="item-name">Sweet &amp; Sour Braised Chicken</span><span class="leader"></span><span class="price">$9.90</span></li>
        <li class="item"><span class="item-name">Sweet &amp; Sour Chicken Fritters</span><span class="leader"></span><span class="price">$9.90</span></li>
        <li class="item"><span class="item-name">Sweet &amp; Sour Combination <small>(Beef, Chicken &amp; King Prawn)</small></span><span class="leader"></span><span class="price">$11.00</span></li>
        <li class="item"><span class="item-name">Sweet &amp; Sour King Prawns Fritters</span><span class="leader"></span><span class="price">$11.50</span></li>
      </ul>
    </section>

    <section class="section" style="--top:1528px">
      <h2 class="section-title">King Prawns</h2>
      <ul class="items">
        <li class="item"><span class="item-name">King Prawns with Vegetables</span><span class="leader"></span><span class="price">$9.90</span></li>
        <li class="item"><span class="item-name">King Prawns with Black Bean Sauce</span><span class="leader"></span><span class="price">$9.90</span></li>
        <li class="item"><span class="item-name">Curried King Prawns with Vegetables</span><span class="leader"></span><span class="price">$9.90</span></li>
        <li class="item"><span class="item-name">King Prawn Cutlets (6)</span><span class="leader"></span><span class="price">$9.90</span></li>
        <li class="item"><span class="item-name">King Prawns with Cashew Nuts</span><span class="leader"></span><span class="price">$10.30</span></li>
        <li class="item"><span class="item-name">King Prawns with Almonds</span><span class="leader"></span><span class="price">$10.30</span></li>
        <li class="item"><span class="item-name">King Prawn Combination</span><span class="leader"></span><span class="price">$10.50</span></li>
        <li class="item"><span class="item-name">King Prawns with Ginger &amp; Shallot</span><span class="leader"></span><span class="price">$11.50</span></li>
        <li class="item"><span class="item-name">Garlic King Prawns</span><span class="leader"></span><span class="price">$11.50</span></li>
        <li class="item"><span class="item-name">Sate King Prawns</span><span class="leader"></span><span class="price">$11.50</span></li>
        <li class="item"><span class="item-name">King Prawns with Chilli Sauce</span><span class="leader"></span><span class="price">$11.50</span></li>
        <li class="item"><span class="item-name">Honey King Prawns</span><span class="leader"></span><span class="price">$11.50</span></li>
        <li class="item"><span class="item-name">King Prawn Fritters</span><span class="leader"></span><span class="price">$11.50</span></li>
        <li class="item"><span class="item-name">King Prawns with Szechuan Sauce (Hot)</span><span class="leader"></span><span class="price">$11.50</span></li>
        <li class="item"><span class="item-name">Crispy King Prawns with Salt and Pepper</span><span class="leader"></span><span class="price">$11.50</span></li>
        <li class="item"><span class="item-name">King Prawns with Garlic and Chilli Sauce</span><span class="leader"></span><span class="price">$11.50</span></li>
        <li class="item"><span class="item-name">King Prawns with Sweet Chilli Sauce</span><span class="leader"></span><span class="price">$11.50</span></li>
      </ul>
    </section>

    <section class="section" style="--top:2002px">
      <h2 class="section-title">Seafood</h2>
      <ul class="items">
        <li class="item"><span class="item-name">Salt &amp; Pepper Squid</span><span class="leader"></span><span class="price">$10.00</span></li>
        <li class="item"><span class="item-name">Seafood Combination with Ginger &amp; Shallot</span><span class="leader"></span><span class="price">$12.00</span></li>
        <li class="item"><span class="item-name">Braised Scallops with Garlic Sauce</span><span class="leader"></span><span class="price">$12.00</span></li>
        <li class="item"><span class="item-name">Braised Scallops with Sate Sauce</span><span class="leader"></span><span class="price">$12.00</span></li>
        <li class="item"><span class="item-name">Braised Scallops with BBQ Sauce</span><span class="leader"></span><span class="price">$12.00</span></li>
        <li class="item"><span class="item-name">Braised Scallops with Mushrooms and Baby Corn</span><span class="leader"></span><span class="price">$12.00</span></li>
        <li class="item"><span class="item-name">Seafood Combination with Black Bean Sauce</span><span class="leader"></span><span class="price">$12.00</span></li>
        <li class="item"><span class="item-name">Seafood Combination with Oyster Sauce</span><span class="leader"></span><span class="price">$12.00</span></li>
        <li class="item"><span class="item-name">Seafood Combination with Sate Sauce</span><span class="leader"></span><span class="price">$12.00</span></li>
        <li class="item"><span class="item-name">Seafood Combination with Garlic and Chilli Sauce</span><span class="leader"></span><span class="price">$12.00</span></li>
      </ul>
    </section>
  </div>

  <div class="column column-right">
    <section class="section" style="--top:430px">
      <h2 class="section-title">Beef</h2>
      <ul class="items">
        <li class="item"><span class="item-name">Beef with Curry Sauce</span><span class="leader"></span><span class="price">$8.80</span></li>
        <li class="item"><span class="item-name">Beef with Black Bean Sauce</span><span class="leader"></span><span class="price">$8.80</span></li>
        <li class="item"><span class="item-name">Beef with Vegetables</span><span class="leader"></span><span class="price">$8.80</span></li>
        <li class="item"><span class="item-name">Beef with Almonds</span><span class="leader"></span><span class="price">$9.30</span></li>
        <li class="item"><span class="item-name">Beef with Cashew Nuts</span><span class="leader"></span><span class="price">$9.30</span></li>
        <li class="item"><span class="item-name">Beef with Ginger &amp; Shallot</span><span class="leader"></span><span class="price">$9.90</span></li>
        <li class="item"><span class="item-name">Beef with Oyster Sauce</span><span class="leader"></span><span class="price">$9.90</span></li>
        <li class="item"><span class="item-name">Beef with Garlic Sauce</span><span class="leader"></span><span class="price">$9.90</span></li>
        <li class="item"><span class="item-name">Beef with Garlic and Chilli Sauce</span><span class="leader"></span><span class="price">$9.90</span></li>
        <li class="item"><span class="item-name">Beef with Mongolian Sauce</span><span class="leader"></span><span class="price">$9.90</span></li>
        <li class="item"><span class="item-name">Beef with Black Pepper Sauce</span><span class="leader"></span><span class="price">$9.90</span></li>
        <li class="item"><span class="item-name">Beef with Sate Sauce</span><span class="leader"></span><span class="price">$9.90</span></li>
        <li class="item"><span class="item-name">Beef with Chilli Sauce</span><span class="leader"></span><span class="price">$9.90</span></li>
        <li class="item"><span class="item-name">Beef with Barbecue Sauce</span><span class="leader"></span><span class="price">$9.90</span></li>
        <li class="item"><span class="item-name">Beef with Szechaun Sauce (Hot)</span><span class="leader"></span><span class="price">$9.90</span></li>
      </ul>
    </section>

    <section class="section" style="--top:855px">
      <h2 class="section-title">Lamb</h2>
      <ul class="items">
        <li class="item"><span class="item-name">Mongolian Lamb Fillet</span><span class="leader"></span><span class="price">$10.80</span></li>
        <li class="item"><span class="item-name">Lamb with BBQ Sauce</span><span class="leader"></span><span class="price">$10.80</span></li>
        <li class="item"><span class="item-name">Lamb with Szechuan Sauce (Hot)</span><span class="leader"></span><span class="price">$10.80</span></li>
        <li class="item"><span class="item-name">Lamb with Garlic and Chilli Sauce</span><span class="leader"></span><span class="price">$10.80</span></li>
        <li class="item"><span class="item-name">Lamb with Sate Sauce</span><span class="leader"></span><span class="price">$10.80</span></li>
        <li class="item"><span class="item-name">Lamb with Garlic Sauce</span><span class="leader"></span><span class="price">$10.80</span></li>
        <li class="item"><span class="item-name">Lamb with Black Pepper Sauce</span><span class="leader"></span><span class="price">$10.80</span></li>
        <li class="item"><span class="item-name">Deep Fried Lamb Fillet with Special Sauce</span><span class="leader"></span><span class="price">$10.80</span></li>
      </ul>
    </section>

    <section class="section" style="--top:1104px">
      <h2 class="section-title">Chicken</h2>
      <ul class="items">
        <li class="item"><span class="item-name">Braised Chicken with Curry Sauce</span><span class="leader"></span><span class="price">$8.80</span></li>
        <li class="item"><span class="item-name">Braised Chicken with Vegetables</span><span class="leader"></span><span class="price">$8.80</span></li>
        <li class="item"><span class="item-name">Braised Chicken with Black Bean Sauce</span><span class="leader"></span><span class="price">$8.80</span></li>
        <li class="item"><span class="item-name">Braised Chicken with Cashew Nuts</span><span class="leader"></span><span class="price">$9.30</span></li>
        <li class="item"><span class="item-name">Braised Chicken with Almonds</span><span class="leader"></span><span class="price">$9.30</span></li>
        <li class="item"><span class="item-name">Garlic Butter Chicken</span><span class="leader"></span><span class="price">$9.90</span></li>
        <li class="item"><span class="item-name">Braised Chicken with Ginger &amp; Shallot</span><span class="leader"></span><span class="price">$9.90</span></li>
        <li class="item"><span class="item-name">Braised Chicken with Sate Sauce</span><span class="leader"></span><span class="price">$9.90</span></li>
        <li class="item"><span class="item-name">Lemon Chicken Fritters</span><span class="leader"></span><span class="price">$9.90</span></li>
        <li class="item"><span class="item-name">Honey Chicken Fritters</span><span class="leader"></span><span class="price">$9.90</span></li>
        <li class="item"><span class="item-name">Braised Chicken in Garlic Sauce</span><span class="leader"></span><span class="price">$9.90</span></li>
        <li class="item"><span class="item-name">Braised Chicken with Chilli Sauce</span><span class="leader"></span><span class="price">$9.90</span></li>
        <li class="item"><span class="item-name">Braised Chicken with Garlic and Chilli Sauce</span><span class="leader"></span><span class="price">$9.90</span></li>
        <li class="item"><span class="item-name">Braised Chicken with Sweet Chilli Sauce</span><span class="leader"></span><span class="price">$9.90</span></li>
        <li class="item"><span class="item-name">Braised Chicken with Szechuan Sauce (Hot)</span><span class="leader"></span><span class="price">$9.90</span></li>
      </ul>
    </section>

    <section class="section" style="--top:1530px">
      <h2 class="section-title">Pork</h2>
      <ul class="items">
        <li class="item"><span class="item-name">Pork with Black Bean Sauce</span><span class="leader"></span><span class="price">$8.80</span></li>
        <li class="item"><span class="item-name">Pork with Vegetables</span><span class="leader"></span><span class="price">$8.80</span></li>
        <li class="item"><span class="item-name">Pork with Almonds</span><span class="leader"></span><span class="price">$9.30</span></li>
        <li class="item"><span class="item-name">Pork with Cashew Nuts</span><span class="leader"></span><span class="price">$9.30</span></li>
        <li class="item"><span class="item-name">Pork with Ginger &amp; Shallot</span><span class="leader"></span><span class="price">$9.90</span></li>
        <li class="item"><span class="item-name">Pork with Szechuan Sauce (Hot)</span><span class="leader"></span><span class="price">$9.90</span></li>
        <li class="item"><span class="item-name">Pork with BBQ Sauce</span><span class="leader"></span><span class="price">$9.90</span></li>
        <li class="item"><span class="item-name">Pork with Garlic Sauce</span><span class="leader"></span><span class="price">$9.90</span></li>
        <li class="item"><span class="item-name">Pork with Chilli Sauce</span><span class="leader"></span><span class="price">$9.90</span></li>
        <li class="item"><span class="item-name">Pork with Sate Sauce</span><span class="leader"></span><span class="price">$9.90</span></li>
        <li class="item"><span class="item-name">Pork with Mongolian Sauce</span><span class="leader"></span><span class="price">$9.90</span></li>
        <li class="item"><span class="item-name">Pork with Sweet Chilli Sauce</span><span class="leader"></span><span class="price">$9.90</span></li>
        <li class="item"><span class="item-name">BBQ Pork with Plum Sauce</span><span class="leader"></span><span class="price">$9.90</span></li>
        <li class="item"><span class="item-name">BBQ Pork with Black Bean Sauce</span><span class="leader"></span><span class="price">$9.90</span></li>
        <li class="item"><span class="item-name">Salt &amp; Pepper Pork</span><span class="leader"></span><span class="price">$10.00</span></li>
      </ul>
    </section>

    <section class="section" style="--top:1958px">
      <h2 class="section-title light">Vegetables</h2>
      <ul class="items">
        <li class="item"><span class="item-name">Stir-Fried Mixed Vegetables</span><span class="leader"></span><span class="price">$7.00</span></li>
        <li class="item"><span class="item-name">Steamed Mixed Vegetables w/ Oyster Sauce</span><span class="leader"></span><span class="price">$7.00</span></li>
        <li class="item"><span class="item-name">Mixed Vegetables w/ Curry Sauce</span><span class="leader"></span><span class="price">$7.00</span></li>
        <li class="item"><span class="item-name">Mixed Vegetables w/ Black Bean Sauce</span><span class="leader"></span><span class="price">$7.00</span></li>
        <li class="item"><span class="item-name">Mixed Vegetables w/ Baby Corn &amp; Mushrooms</span><span class="leader"></span><span class="price">$8.00</span></li>
        <li class="item"><span class="item-name">Broccoli w/ Crabmeat Sauce</span><span class="leader"></span><span class="price">$8.80</span></li>
      </ul>
    </section>
  </div>

  <svg class="guardian-art" viewBox="0 0 370 140" role="img" aria-label="Illustration of a stone guardian lion statue on a pedestal with curling black flourishes">
    <defs>
      <linearGradient id="guardian-tone" x1="0" y1="0" x2="0" y2="1">
        <stop offset="0" stop-color="#f3ece1"/>
        <stop offset="1" stop-color="#d9cfc2"/>
      </linearGradient>
    </defs>
    <rect x="120" y="0" width="130" height="140" rx="14" fill="url(#guardian-tone)"/>
  </svg>
  <p class="established">EST. 1976</p>

  <p class="serving-note">All dishes served with: Fried Rice, Boiled Rice OR Soft Noodles<br>OR Thick Rice Noodles $1.50 extra</p>
</main>
</body>
</html>
```